Velmoro Cabinets Letter Head and Email Signature

Hi
I would love a design package for a letterhead, email signature, even update my business card if you like if you can come up with a great idea for my new high end cabinet shop. Velmoro Cabinets brings timeless craftsmanship to modern interiors, specializing in high end, custom cabinetry designed for architects and interior designers.

Target Market(s)

high end, luxury market

Industry/Entity Type

cabinet making

Requirements
Must have
• my colours of logo as the theme

```html
<!DOCTYPE html>
<html lang="en">
<head>
<meta charset="utf-8">
<title>Velmoro Cabinets – Letterhead and Email Signatures</title>
<link href="https://fonts.googleapis.com/css2?family=Lato:wght@400;700&family=Quicksand:wght@400;500&display=swap" rel="stylesheet">
<style>
  :root {
    --backdrop: #959595;
    --charcoal: #363636;
    --green: #4b8a3f;
    --white: #ffffff;
    --paper: #ffffff;
    --ink: #4a4a4a;
    --label: #1c1c1c;
    --signature-blue: #c9d6e8;
  }
  * { margin: 0; padding: 0; box-sizing: border-box; }
  html, body { width: 1200px; height: 807px; overflow: hidden; }
  body { background: var(--backdrop); position: relative; font-family: 'Lato', sans-serif; }

  .brand-name {
    font-family: 'Lato', sans-serif;
    font-weight: 400;
    color: var(--green);
    white-space: nowrap;
    display: flex;
    align-items: center;
    line-height: 1;
  }
  .brand-name .brand-square {
    display: inline-block;
    border: 2px solid var(--green);
    margin-right: 8px;
    flex: none;
  }

  .contact-list { list-style: none; color: var(--white); }
  .contact-list li { display: flex; align-items: center; white-space: nowrap; }
  .contact-list svg { fill: var(--green); flex: none; }

  /* Letterhead */
  .letterhead {
    position: absolute; left: 55px; top: 50px; width: 477px; height: 674px;
    background: var(--paper);
  }
  .letterhead-header {
    position: absolute; left: 0; top: 0; width: 100%; height: 90px;
    background: var(--charcoal);
  }
  .letterhead-header .header-rule {
    position: absolute; left: 0; top: 84px; width: 100%; height: 2px; background: var(--green);
  }
  .letterhead-header .brand-name { position: absolute; left: 38px; top: 36px; font-size: 16px; }
  .letterhead-header .brand-square { width: 14px; height: 14px; margin-right: 7px; border-width: 1.5px; }
  .letterhead-header .contact-list { position: absolute; left: 315px; top: 28px; font-family: 'Quicksand', sans-serif; font-size: 7.5px; }
  .letterhead-header .contact-list li { height: 10px; }
  .letterhead-header .contact-list svg { width: 7px; height: 7px; margin-right: 5px; }

  .letter-body {
    position: absolute; left: 45px; top: 187px; width: 392px;
    font-family: 'Quicksand', sans-serif; color: var(--ink);
  }
  .letter-salutation { font-size: 12px; font-weight: 500; margin-bottom: 23px; }
  .letter-body p.copy { font-size: 7.2px; line-height: 10.1px; margin-bottom: 10.4px; text-align: justify; }
  .letter-closing { font-size: 7px; margin-top: 18px; }
  .signature-area {
    position: absolute; left: 40px; top: 466px; width: 85px; height: 36px;
    background: linear-gradient(90deg, var(--signature-blue), #e4ebf4);
    border-radius: 4px;
  }

  /* Email signatures */
  .email-signature { position: absolute; background: var(--charcoal); overflow: hidden; }
  .signature-wide { left: 581px; top: 116px; width: 529px; height: 202px; }
  .signature-tall { left: 581px; top: 380px; width: 269px; height: 325px; }

  .email-signature .brand-name { position: absolute; font-size: 21px; }
  .email-signature .brand-square { width: 19px; height: 19px; }
  .signature-wide .brand-name { left: 42px; top: 94px; }
  .signature-wide .divider { position: absolute; left: 260px; top: 56px; width: 1px; height: 98px; background: var(--green); }
  .signature-tall .brand-name { left: 31px; top: 60px; }

  .person-name { position: absolute; color: var(--green); font-size: 21px; font-weight: 700; white-space: nowrap; }
  .person-role { position: absolute; color: var(--white); font-size: 13px; white-space: nowrap; }
  .email-signature .contact-list { position: absolute; font-size: 13.3px; }
  .email-signature .contact-list li { height: 16.5px; }
  .email-signature .contact-list svg { width: 10px; height: 10px; margin-right: 8px; }

  .signature-wide .person-name { left: 281px; top: 46px; }
  .signature-wide .person-role { left: 281px; top: 72px; }
  .signature-wide .contact-list { left: 281px; top: 104px; }
  .signature-tall .person-name { left: 33px; top: 139px; }
  .signature-tall .person-role { left: 33px; top: 165px; }
  .signature-tall .contact-list { left: 31px; top: 216px; }

  .piece-label { position: absolute; color: var(--label); font-size: 12.5px; font-weight: 700; white-space: nowrap; }
  .label-letterhead { left: 276px; top: 731px; transform: translateX(-50%); }
  .label-signature-wide { left: 834px; top: 332px; transform: translateX(-50%); }
  .label-signature-tall { left: 610px; top: 723px; }
</style>
</head>
<body>

<section class="letterhead">
  <header class="letterhead-header">
    <div class="brand-name"><span class="brand-square"></span>Velmoro Cabinets</div>
    <ul class="contact-list">
      <li><svg viewBox="0 0 10 10"><path d="M2 0.5 L3.6 2.6 L2.7 3.8 Q3.6 5.8 6.2 7.3 L7.4 6.4 L9.5 8 L8.4 9.5 Q3.5 9 0.5 1.6 Z"/></svg>0400 518 274</li>
      <li><svg viewBox="0 0 10 10"><path d="M0.5 2 H9.5 V8.5 H0.5 Z"/><path d="M1.2 2.6 L5 5.5 L8.8 2.6" fill="none" stroke="#363636" stroke-width="0.8"/></svg>info@velmorocabinets.com.au</li>
      <li><svg viewBox="0 0 10 10"><circle cx="5" cy="5" r="4.6"/></svg>www.velmorocabinets.com.au</li>
    </ul>
    <div class="header-rule"></div>
  </header>

  <div class="letter-body">
    <p class="letter-salutation">Dear Mr. Ainsley,</p>
    <p class="copy">Lorem ipsum dolor sit amet, consectetur adipiscing elit. Donec orci purus, luctus vitae dignissim eu, iaculis sed purus. Vivamus faucibus, ipsum nec aliquet viverra, leo mauris condimentum ligula, sit amet sagittis enim ligula quis arcu. Nam egestas tortor id nisi porttitor mattis. In tortor ante, ultricies in suscipit a, tempus non massa. Fusce vel massa nulla.</p>
    <p class="copy">Donec malesuada orci vitae nulla accumsan porta a id massa. Quisque accumsan iaculis magna sit amet fringilla. Maecenas consequat, magna eget tincidunt semper, odio nibh rutrum mi, id feugiat ante nisi eu risus. Vestibulum nunc orci, rhoncus a placerat in, ultricies in mi. Cras mattis varius eros.</p>
    <p class="copy">Sed id augue vitae urna euismod commodo aliquet a quam. Pellentesque arcu velit, cursus et malesuada ut, consequat et diam. Nullam erat sem, rhoncus id ullamcorper vitae, rhoncus et arcu. In ultricies ultricies nulla, ut rutrum nisi iaculis at. Donec eu magna a metus ornare faucibus. Morbi semper, est id tincidunt gravida, sem arcu adipiscing lacus, ac bibendum nulla leo eu purus. Vestibulum id purus lorem.</p>
    <p class="copy">It is a long established fact that a reader will be distracted by the readable content of a page when looking at its layout. The point of using placeholder text is that it has a more or less normal spread of letters, making it look like readable English.</p>
    <p class="letter-closing">Sincerely,</p>
  </div>
  <div class="signature-area" role="img" aria-label="Handwritten signature of the sender"></div>
</section>
<div class="piece-label label-letterhead">Letterhead</div>

<section class="email-signature signature-wide">
  <div class="brand-name"><span class="brand-square"></span>Velmoro Cabinets</div>
  <div class="divider"></div>
  <div class="person-name">Marcus Delaney</div>
  <div class="person-role">Director Craftsman</div>
  <ul class="contact-list">
    <li><svg viewBox="0 0 10 10"><path d="M2 0.5 L3.6 2.6 L2.7 3.8 Q3.6 5.8 6.2 7.3 L7.4 6.4 L9.5 8 L8.4 9.5 Q3.5 9 0.5 1.6 Z"/></svg>0400 518 274</li>
    <li><svg viewBox="0 0 10 10"><path d="M0.5 2 H9.5 V8.5 H0.5 Z"/><path d="M1.2 2.6 L5 5.5 L8.8 2.6" fill="none" stroke="#363636" stroke-width="0.8"/></svg>info@velmorocabinets.com.au</li>
    <li><svg viewBox="0 0 10 10"><circle cx="5" cy="5" r="4.6"/></svg>www.velmorocabinets.com.au</li>
  </ul>
</section>
<div class="piece-label label-signature-wide">Email Signature 1</div>

<section class="email-signature signature-tall">
  <div class="brand-name"><span class="brand-square"></span>Velmoro Cabinets</div>
  <div class="person-name">Marcus Delaney</div>
  <div class="person-role">Director Craftsman</div>
  <ul class="contact-list">
    <li><svg viewBox="0 0 10 10"><path d="M2 0.5 L3.6 2.6 L2.7 3.8 Q3.6 5.8 6.2 7.3 L7.4 6.4 L9.5 8 L8.4 9.5 Q3.5 9 0.5 1.6 Z"/></svg>0400 518 274</li>
    <li><svg viewBox="0 0 10 10"><path d="M0.5 2 H9.5 V8.5 H0.5 Z"/><path d="M1.2 2.6 L5 5.5 L8.8 2.6" fill="none" stroke="#363636" stroke-width="0.8"/></svg>info@velmorocabinets.com.au</li>
    <li><svg viewBox="0 0 10 10"><circle cx="5" cy="5" r="4.6"/></svg>www.velmorocabinets.com.au</li>
  </ul>
</section>
<div class="piece-label label-signature-tall">Email Signature 2</div>

</body>
</html>
```